Alumni Ballot Postcard

We need a quick postcard to mail out to our alumni telling them that they are invited to vote on a new ballot of alumni officers. I purchased a 4 color picture I want to use for the front of the postcard from pixbarn but I can't get it to upload. Someone can email me at Marta.venn@sgfcollege-example.edu and I will email them the image. The final design needs to be clean and easy to read.

Offering doctoral, master’s, baccalaureate, and associate degrees, Saint Gideon of the Fields College is a four-year, independent Catholic institution, providing a strong foundation in the liberal arts and continuing its highly-regarded health sciences and nursing programs.

```html
<!DOCTYPE html>
<html lang="en">
<head>
<meta charset="utf-8">
<title>Alumni Ballot Postcard – Saint Gideon of the Fields College</title>
<link href="https://fonts.googleapis.com/css2?family=Cinzel:wght@600;700&family=Lato:wght@400;700;900&display=swap" rel="stylesheet">
<style>
  :root {
    --canvas-bg: #e9e6e1;
    --card-white: #ffffff;
    --navy: #133a6b;
    --blue: #2a6cb3;
    --blue-deep: #0f3d78;
    --sky: #5aa9e0;
    --ink: #2d2d2d;
    --panel-dark: #1c1c1c;
    --panel-mid: #3a3a3a;
    --link: #5ab0ee;
    --line: #555555;
  }
  * { margin: 0; padding: 0; box-sizing: border-box; }
  html, body { width: 902px; height: 1200px; overflow: hidden; }
  body {
    background: var(--canvas-bg);
    position: relative;
    font-family: "Lato", Arial, sans-serif;
  }

  .postcard {
    position: absolute;
    left: 105px;
    width: 676px;
    height: 522px;
    background: var(--card-white);
    overflow: hidden;
    box-shadow: 0 2px 8px rgba(0,0,0,0.18);
  }
  .postcard--front { top: 50px; }
  .postcard--back  { top: 620px; }

  /* Front */
  .front-photo {
    position: absolute; inset: 0;
    background:
      radial-gradient(ellipse 170px 140px at 62% 52%, #2f7fc8 0%, #2a6cb3 55%, transparent 100%),
      linear-gradient(135deg, #4a4c50 0%, #2b2c2f 45%, #3c3e42 70%, #1e1f22 100%);
  }
  .front-wave { position: absolute; left: 0; top: 330px; width: 676px; height: 192px; }
  .front-title {
    position: absolute; left: 60px; top: 395px;
  }
  .front-title__kicker {
    font-family: "Lato", Arial, sans-serif;
    font-weight: 900;
    font-size: 42px;
    color: var(--ink);
    line-height: 1;
  }
  .front-title__headline {
    font-family: "Cinzel", Georgia, serif;
    font-weight: 600;
    font-size: 46px;
    color: var(--navy);
    line-height: 1.1;
    margin-top: 8px;
  }

  /* Back */
  .back-column { position: absolute; left: 0; top: 0; width: 325px; height: 522px; }
  .intro-panel {
    position: absolute; left: 0; top: 0; width: 325px; height: 147px;
    background: linear-gradient(90deg, #1d5fa8 0%, #2a6cb3 50%, #0c2f60 100%);
    color: #fff;
    font-weight: 700;
    font-size: 14px;
    line-height: 1.3;
    padding: 18px 24px 0 22px;
    text-align: justify;
  }
  .college-name {
    position: absolute; left: 28px; top: 166px;
    display: flex; align-items: center; gap: 16px;
  }
  .college-name__mark {
    width: 30px; height: 30px; background: var(--panel-dark);
  }
  .college-name__text {
    font-family: "Cinzel", Georgia, serif;
    font-weight: 600;
    font-size: 25px;
    line-height: 1.06;
    color: var(--panel-dark);
  }
  .info-panel {
    position: absolute; left: 0; top: 276px; width: 325px; height: 168px;
    background: linear-gradient(90deg, #111 0%, var(--panel-mid) 100%);
    color: #fff;
    font-size: 12.6px;
    line-height: 1.3;
    padding: 9px 14px 0 22px;
  }
  .info-panel p + p { margin-top: 12px; }
  .info-panel a { color: var(--link); font-weight: 700; text-decoration: none; }
  .cta-band {
    position: absolute; left: 0; top: 448px; width: 325px; height: 74px;
    background: var(--sky);
    font-family: "Cinzel", Georgia, serif;
    font-weight: 700;
    font-size: 18px;
    color: var(--navy);
    text-align: center;
    line-height: 1.2;
    padding-top: 14px;
  }
  .stamp-box {
    position: absolute; left: 593px; top: 23px; width: 63px; height: 74px;
    border: 1.5px solid var(--ink);
  }
  .address-line {
    position: absolute; left: 425px; width: 231px; height: 1.5px; background: var(--line);
  }
</style>
</head>
<body>

  <section class="postcard postcard--front" aria-label="Postcard front">
    <div class="front-photo" role="img" aria-label="Photograph: close-up of a dark computer keyboard with a blue Enter key labelled Vote"></div>
    <svg class="front-wave" viewBox="0 0 676 192" aria-hidden="true">
      <path d="M0 60 C100 10 250 0 400 55 C500 92 600 120 676 140 L676 192 L0 192 Z" fill="#ffffff"/>
      <path d="M0 60 C100 10 250 0 400 55 C500 92 600 120 676 140" fill="none" stroke="var(--blue-deep)" stroke-width="8"/>
      <path d="M0 68 C100 20 250 10 400 64 C500 100 600 128 676 148" fill="none" stroke="var(--blue)" stroke-width="4" opacity="0.6"/>
    </svg>
    <div class="front-title">
      <div class="front-title__kicker">Alumni:</div>
      <div class="front-title__headline">Please Vote!</div>
    </div>
  </section>

  <section class="postcard postcard--back" aria-label="Postcard back">
    <div class="back-column">
      <div class="intro-panel">
        Over the past year and a half, the Alumni Association Executive Committee has been working on a major revision to the Alumni Association bylaws. The goal is a stronger and more inclusive Alumni Association.
      </div>

      <div class="college-name">
        <span class="college-name__mark" aria-hidden="true"></span>
        <span class="college-name__text">Saint Gideon<br>of the Fields<br>College</span>
      </div>

      <div class="info-panel">
        <p>In order to confirm the new bylaws we need alumni approval.</p>
        <p>Go to <a href="#">sgfcollege-example.edu/alumni-feedback</a> to give us your responses to the proposed bylaws and to vote on a new slate of officers.</p>
        <p>Email <a href="#">AlumniAssoc@sgfcollege-example.edu</a> if you have questions.</p>
      </div>

      <div class="cta-band">We value your opinion.<br>Vote today!</div>
    </div>

    <div class="stamp-box" aria-label="Stamp area"></div>
    <div class="address-line" style="top:282px"></div>
    <div class="address-line" style="top:335px"></div>
    <div class="address-line" style="top:388px"></div>
  </section>

</body>
</html>
```